What makes us Different Managed Communications Services Provider Flyer

We need a flyer to explain why we are different than other "managed IT services" company. Gives a brief description of our company and services that can entice clients and potential clients to setup a FREE consultation with us. This will become part of an ongoing marketing campaign that includes emails, leave behinds, brochures, and more

```html
<!DOCTYPE html>
<html lang="en">
<head>
<meta charset="utf-8">
<title>Summit Line Networks – Flyer</title>
<link rel="stylesheet" href="https://fonts.googleapis.com/css2?family=Oswald:wght@600;700&family=Montserrat:wght@400;600;700;800&display=swap">
<style>
  :root{
    --page-bg:#e6e7ea;
    --paper:#ffffff;
    --paper-tint:#f2f4f8;
    --blue-deep:#1b4fb8;
    --blue-mid:#1f7fd6;
    --cyan:#1fb8e6;
    --ink:#2a2f3a;
    --ink-soft:#4b5160;
    --photo-a:#cfd9e6;
    --photo-b:#8ea3bd;
  }
  *{box-sizing:border-box;margin:0;padding:0}
  html,body{width:1200px;height:800px;overflow:hidden;background:var(--page-bg)}
  body{font-family:"Montserrat",sans-serif;color:var(--ink);position:relative}
  .flyer{position:absolute;left:320px;top:15px;width:560px;height:770px;background:linear-gradient(180deg,var(--paper) 0%,var(--paper-tint) 100%);box-shadow:0 6px 24px rgba(0,0,0,.18);overflow:hidden}
  .header-art{position:absolute;left:0;top:0;width:560px;height:300px}
  .brand{position:absolute;left:34px;top:128px;display:flex;align-items:center;gap:7px;font-family:"Montserrat",sans-serif;font-weight:700;font-size:13px;color:var(--blue-deep)}
  .brand-mark{width:14px;height:14px;background:var(--blue-deep)}
  .headline{position:absolute;left:34px;top:206px;font-family:"Oswald",sans-serif;font-weight:700;font-size:20px;line-height:1.12;color:#fff;text-transform:uppercase;letter-spacing:.3px;white-space:nowrap}
  .intro{position:absolute;left:34px;top:305px;width:492px;font-size:8.6px;line-height:1.45;color:var(--ink)}
  .columns{position:absolute;left:34px;top:392px;width:492px;display:grid;grid-template-columns:1fr 1fr;column-gap:24px}
  .section{margin-bottom:10px}
  .section-title{font-weight:800;font-size:11px;color:var(--blue-mid);margin-bottom:4px;line-height:1.15}
  .section-title.caps{text-transform:uppercase}
  .section p{font-size:7.6px;line-height:1.45;color:var(--ink-soft);margin-bottom:5px}
  b{color:var(--ink);font-weight:700}
  .services{list-style:none}
  .services li{position:relative;padding-left:12px;font-size:7.6px;line-height:1.42;color:var(--ink-soft);margin-bottom:3px}
  .services li::before{content:"";position:absolute;left:0;top:2px;width:7px;height:7px;border-radius:50%;background:var(--blue-mid)}
  .footer-band{position:absolute;left:0;bottom:0;width:560px;height:78px}
  .contact{position:absolute;left:120px;bottom:22px;display:flex;gap:26px;font-size:11.5px;color:#fff;font-weight:600}
  .contact span{display:flex;align-items:center;gap:6px}
  .contact svg{width:14px;height:14px}
</style>
</head>
<body>
<main class="flyer">
  <svg class="header-art" viewBox="0 0 560 300">
    <defs>
      <linearGradient id="photoTone" x1="0" y1="0" x2="1" y2="1">
        <stop offset="0" stop-color="var(--photo-a)"/>
        <stop offset="1" stop-color="var(--photo-b)"/>
      </linearGradient>
      <linearGradient id="bandBlue" x1="0" y1="0" x2="1" y2="0">
        <stop offset="0" stop-color="var(--blue-deep)"/>
        <stop offset="1" stop-color="var(--cyan)"/>
      </linearGradient>
    </defs>
    <polygon points="150,0 560,0 560,225 370,225" fill="url(#photoTone)" role="img" aria-label="Photo of a smiling business team gathered around a meeting table in a bright office"/>
    <polygon points="250,110 280,110 362,236 560,236 560,244 354,244" fill="var(--blue-mid)"/>
    <polygon points="270,160 302,160 336,192 304,192" fill="var(--cyan)"/>
    <polygon points="0,192 372,192 330,290 0,290" fill="url(#bandBlue)"/>
  </svg>

  <div class="brand"><span class="brand-mark"></span>Summit Line Networks</div>

  <h1 class="headline">More than just a<br>managed IT provider –<br>our legacy of excellence</h1>

  <p class="intro">At our company, we are far more than your typical managed IT provider. Since our founding in 1983, we have built a reputation based on trust, reliability, and unparalleled service. With <b>client relationships spanning 20 to 30 years</b>, we have demonstrated a level of commitment that few IT firms can match. What sets us apart is not just our technical expertise but the <b>deep, long-term partnerships</b> we cultivate with our clients—many of whom have stayed with us <b>without ever being locked into a contract.</b> That is a testament to the exceptional quality of our service and the trust we have earned over decades.</p>

  <div class="columns">
    <div class="col">
      <section class="section">
        <h2 class="section-title caps">A Commitment Beyond Contracts</h2>
        <p>Unlike many managed IT providers who rely on rigid contracts to retain clients, we believe that service excellence speaks for itself. The longevity of our client relationships is rooted in our ability to anticipate needs, resolve challenges before they escalate, and proactively enhance network &amp; communication infrastructures. Our comprehensive checklists, questionnaires, policies, and procedures, attention to details ensure that every client receives a tailored, best-in-class experience from day one.</p>
      </section>
      <section class="section">
        <h2 class="section-title">A Holistic Approach to IT Management</h2>
        <p>We don't just manage IT—we integrate ourselves into your business, ensuring that technology aligns with your strategic goals. Our services go beyond traditional break-fix support; we offer:</p>
        <ul class="services">
          <li><b>Strategic IT Roadmaps</b> customized to drive business growth.</li>
          <li><b>Proactive cybersecurity assessments</b> that help keep businesses secure.</li>
          <li><b>Comprehensive backup &amp; disaster recovery solutions</b> that provide peace of mind.</li>
          <li><b>Industry-leading response times &amp; dedicated support teams</b> focused on delivering an exceptional client</li>
        </ul>
      </section>
    </div>
    <div class="col">
      <section class="section">
        <h2 class="section-title">Our Clients Stay Because We Deliver</h2>
        <p>For over 40 years, we have maintained a standard of excellence that <b>other companies simply cannot compare with.</b> Our team of experts consistently goes above and beyond, ensuring that clients not only <b>get the support they need but also receive the strategic guidance necessary to stay ahead in an ever-evolving digital landscape.</b></p>
        <p>Our <b>90-day performance review</b> process ensures that we continuously improve our service based on client feedback. This process allows us to <b>adapt, refine, and enhance our approach,</b> providing a truly personalized IT experience that aligns with business objectives.</p>
      </section>
      <section class="section">
        <h2 class="section-title">A Legacy of Trust &amp; Reliability</h2>
        <p>The fact that many of our clients have remained with us for <b>decades without a formal contract</b> speaks volumes about the trust we have built. We don't lock in clients with paperwork—we keep them with results. <b>That's the difference between a standard managed IT provider and an IT partner who genuinely cares.</b></p>
        <p>If you're looking for an IT provider that will treat your business as if it were their own, look no further. Our legacy of service, innovation, and commitment to our clients is what sets us apart from the rest.</p>
      </section>
    </div>
  </div>

  <svg class="footer-band" viewBox="0 0 560 78" aria-hidden="true">
    <defs>
      <linearGradient id="footBlue" x1="0" y1="0" x2="1" y2="0">
        <stop offset="0" stop-color="var(--blue-deep)"/>
        <stop offset="1" stop-color="var(--cyan)"/>
      </linearGradient>
    </defs>
    <polygon points="0,10 80,78 0,78" fill="var(--blue-mid)"/>
    <polygon points="70,30 560,30 560,78 110,78" fill="url(#footBlue)"/>
    <polygon points="470,0 560,0 560,30 520,30" fill="var(--cyan)"/>
  </svg>

  <div class="contact">
    <span><svg viewBox="0 0 16 16"><path d="M8 1a5 5 0 0 0-5 5c0 3.8 5 9 5 9s5-5.2 5-9a5 5 0 0 0-5-5zm0 7a2 2 0 1 1 0-4 2 2 0 0 1 0 4z" fill="#fff"/></svg>Riverton, Texas</span>
    <span><svg viewBox="0 0 16 16"><path d="M4 1.5l2 3-1.3 1.3a9 9 0 0 0 5.5 5.5L11.5 10l3 2-1 2.5C7 14.5 1.5 9 1.5 2.5z" fill="#fff"/></svg>(713) 555-0187</span>
    <span><svg viewBox="0 0 16 16" fill="none" stroke="#fff" stroke-width="1.3"><circle cx="8" cy="8" r="6.3"/><ellipse cx="8" cy="8" rx="2.8" ry="6.3"/><path d="M1.7 8h12.6"/></svg>www.summitlinenet.com</span>
  </div>
</main>
</body>
</html>
```